Consulting Company Business Card

I am looking for a minimalist, classy, professional design on my business card. I would like it to be double-sided. I want to use the font and color scheme of my logo which are attached. Please be creative in the designs that you send me. I want to play off the design of my logo with the inner C that is Green and Blue broken up with the white.
Target Market(s)
Small Businesses
Industry/Entity Type
Consulting
Contact Information for Business Card
Derek L. Whitmore, CPA CGMA, 555-014-2283, dwhitmore@brovantadvisory.example, www.brovantadvisory.example

```html
<!DOCTYPE html>
<html lang="en">
<head>
<meta charset="utf-8">
<title>Brovant Advisory – Business Card</title>
<link href="https://fonts.googleapis.com/css2?family=Montserrat:wght@400;500;700;800&display=swap" rel="stylesheet">
<style>
  :root {
    --navy: #2b2f52;
    --navy-deep: #2e3556;
    --teal: #22737a;
    --teal-bright: #2a7f82;
    --white: #ffffff;
    --backdrop: #1f2024;
  }
  * { box-sizing: border-box; margin: 0; padding: 0; }
  html, body {
    width: 1200px; height: 900px; overflow: hidden;
    background: var(--backdrop);
    font-family: "Montserrat", Arial, sans-serif;
  }
  .canvas {
    position: relative; width: 1200px; height: 900px;
    display: flex; flex-direction: column; align-items: center;
    justify-content: center; gap: 50px;
  }
  .card {
    position: relative; width: 630px; height: 360px;
    border-radius: 22px; overflow: hidden;
  }
  .wordmark {
    font-weight: 800; text-transform: uppercase;
    letter-spacing: 2px; line-height: 1.05;
  }

  /* Front */
  .card--front {
    background: linear-gradient(225deg, var(--teal) 0%, #2a4f66 50%, var(--navy-deep) 100%);
    display: flex; align-items: center; justify-content: center;
  }
  .card--front .wordmark { color: var(--white); font-size: 56px; text-align: center; }

  /* Back */
  .card--back { background: var(--white); }
  .back-brand {
    position: absolute; left: 60px; top: 52px;
    display: flex; align-items: center; gap: 26px;
  }
  .brand-dot {
    flex: none; width: 96px; height: 96px; border-radius: 50%;
    background: var(--navy);
  }
  .card--back .wordmark { color: var(--navy); font-size: 42px; }

  .info-band {
    position: absolute; left: 0; right: 0; top: 206px; height: 104px;
    background: linear-gradient(90deg, var(--navy) 0%, var(--navy) 35%, var(--teal-bright) 100%);
    display: flex; align-items: center; padding: 0 26px;
    color: var(--white);
  }
  .holder-name {
    flex: none; font-weight: 700; font-size: 16px; white-space: nowrap;
  }
  .divider {
    flex: none; width: 2px; height: 58px; background: var(--white);
    margin: 0 18px; opacity: .9;
  }
  .contact-list {
    list-style: none; display: flex; flex-direction: column; gap: 6px;
    min-width: 0;
  }
  .contact-item {
    display: flex; align-items: center; gap: 9px;
    font-size: 12px; font-weight: 400; white-space: nowrap;
  }
  .contact-item svg { width: 12px; height: 12px; flex: none; fill: var(--white); }
  .accent-rule {
    position: absolute; left: 0; right: 0; top: 320px; height: 6px;
    background: var(--teal);
  }
</style>
</head>
<body>
<main class="canvas">
  <section class="card card--front" aria-label="Card front">
    <p class="wordmark">Brovant<br>Advisory</p>
  </section>

  <section class="card card--back" aria-label="Card back">
    <div class="back-brand">
      <span class="brand-dot" aria-hidden="true"></span>
      <p class="wordmark">Brovant<br>Advisory</p>
    </div>

    <div class="info-band">
      <p class="holder-name">Derek L. Whitmore, CPA, CGMA</p>
      <span class="divider" aria-hidden="true"></span>
      <ul class="contact-list">
        <li class="contact-item">
          <svg viewBox="0 0 16 16" aria-hidden="true"><path d="M3.5 1.5l2.5 0 1 3.5-1.7 1.2a9 9 0 0 0 4.5 4.5L11 9l3.5 1v2.5c0 1-.8 1.8-1.8 1.8A11.5 11.5 0 0 1 1.7 3.3c0-1 .8-1.8 1.8-1.8z"/></svg>
          555-014-2283
        </li>
        <li class="contact-item">
          <svg viewBox="0 0 16 16" aria-hidden="true"><path d="M1 3h14v10H1z M1.5 3.5L8 9l6.5-5.5" fill="none" stroke="#fff" stroke-width="1.5"/></svg>
          dwhitmore@brovantadvisory.example
        </li>
        <li class="contact-item">
          <svg viewBox="0 0 16 16" aria-hidden="true"><circle cx="8" cy="8" r="6.5" fill="none" stroke="#fff" stroke-width="1.4"/><path d="M1.5 8h13M8 1.5c-3 3.5-3 9.5 0 13M8 1.5c3 3.5 3 9.5 0 13" fill="none" stroke="#fff" stroke-width="1.2"/></svg>
          www.brovantadvisory.example
        </li>
      </ul>
    </div>
    <div class="accent-rule" aria-hidden="true"></div>
  </section>
</main>
</body>
</html>
```